Unique, Impressive, and Modern Business Card

Looking for a distinctive, unique business card. We are distributors of tire repairs supplies, tools, machinery, and chemicals. Our target market are tire repair shops, tire franchises, and mechanic shops. We would like our design to include tire characteristics, and use our business colors. Feel free to use all types design and printing options (emboss, spot uv, foil, etc) QR code may be applied, you can use different size business cards ( standard, square, rounded edge, colored edge, etc), all formats needed for printing, also editable for future changes

Target Market(s)

Automotive, Tire industries

Industry/Entity Type

Tire Industry (automotive)

Contact Information for Business Card

Business logo, business Name (Corvane Supply Inc), Name (Marcus Pellow), Position (President) Address (58 Fernhollow Lane, Brentwood NY 11742), Contact number (Company 1-855-302-4418, Cell 1-631-245-9073, email address (marcus.pellow@corvanesupply.com), URL (www.corvanesupply.com

Requirements
Must have
• Must include Business Colors (Black, Green, Blue, White) see sample website file
Nice to have
• emboss, spot uv, etc

```html
<!DOCTYPE html>
<html lang="en">
<head>
<meta charset="utf-8">
<title>Corvane Supply – Business Card</title>
<link href="https://fonts.googleapis.com/css2?family=Poppins:wght@300;400;600&display=swap" rel="stylesheet">
<style>
  :root {
    --brand-blue: #0a22e6;
    --brand-black: #000000;
    --paper-white: #ffffff;
    --backdrop: #3a3a3a;
  }
  html, body {
    margin: 0;
    padding: 0;
    overflow: hidden;
  }
  .canvas {
    position: relative;
    width: 900px;
    height: 1200px;
    background: var(--backdrop);
    overflow: hidden;
    font-family: "Poppins", sans-serif;
  }
  .card {
    position: absolute;
    top: 301px;
    width: 344px;
    height: 603px;
    overflow: hidden;
  }
  .card-front { left: 70px; background: var(--paper-white); }
  .card-back { left: 500px; width: 345px; background: var(--brand-black); }
  .card-shapes { position: absolute; inset: 0; }

  .brand-mark {
    position: absolute;
    left: 0;
    right: 0;
    display: flex;
    flex-direction: column;
    align-items: center;
  }
  .brand-dot {
    width: 40px;
    height: 40px;
    border-radius: 50%;
    background: var(--brand-blue);
  }
  .brand-name {
    margin-top: 22px;
    font-size: 25px;
    font-weight: 400;
    letter-spacing: 0.5px;
    line-height: 1;
  }
  .card-front .brand-mark { top: 62px; }
  .card-front .brand-name { color: var(--brand-black); }
  .card-back .brand-mark { top: 212px; }
  .card-back .brand-name { color: var(--paper-white); }

  .holder {
    position: absolute;
    top: 283px;
    left: 0;
    right: 0;
    text-align: center;
    color: var(--paper-white);
  }
  .holder-name {
    font-size: 30px;
    font-weight: 600;
    line-height: 1.1;
  }
  .holder-role {
    font-size: 18px;
    font-weight: 300;
    margin-top: 3px;
  }

  .contact-list {
    position: absolute;
    top: 394px;
    left: 61px;
    margin: 0;
    padding: 0;
    list-style: none;
    color: var(--paper-white);
    font-size: 13.5px;
  }
  .contact-item {
    display: flex;
    align-items: center;
    height: 24px;
    margin-bottom: 4px;
  }
  .contact-item.gap { margin-bottom: 9px; }
  .contact-icon {
    width: 24px;
    height: 24px;
    margin-right: 8px;
    flex: none;
  }

  .divider {
    position: absolute;
    top: 336px;
    left: 58px;
    width: 224px;
    height: 2px;
    background: var(--paper-white);
  }
  .back-url {
    position: absolute;
    top: 350px;
    left: 70px;
    display: flex;
    align-items: center;
    color: var(--paper-white);
    font-size: 13.5px;
  }
  .back-url .contact-icon { margin-right: 7px; }
</style>
</head>
<body>
<div class="canvas">

  <section class="card card-front">
    <svg class="card-shapes" width="344" height="603" viewBox="0 0 344 603">
      <polygon points="0,194 344,194 344,274 0,274" fill="var(--brand-black)"/>
      <polygon points="0,274 100,222 172,232 244,218 344,274 344,603 0,603" fill="var(--brand-blue)"/>
      <polygon points="0,0 344,0 344,194 172,232 0,194" fill="var(--paper-white)"/>
    </svg>

    <div class="brand-mark">
      <div class="brand-dot"></div>
      <div class="brand-name">CORVANE SUPPLY</div>
    </div>

    <div class="holder">
      <div class="holder-name">Marcus Pellow</div>
      <div class="holder-role">President</div>
    </div>

    <ul class="contact-list">
      <li class="contact-item">
        <svg class="contact-icon" viewBox="0 0 24 24"><circle cx="12" cy="12" r="12" fill="#fff"/><path d="M8.3 6.5l2 2.3-1.1 1.6c.7 1.6 2 2.9 3.6 3.6l1.6-1.1 2.3 2-1.2 2c-4.3-.3-7.9-3.9-8.2-8.2z" fill="var(--brand-blue)"/></svg>
        1-855-302-4418
      </li>
      <li class="contact-item gap">
        <svg class="contact-icon" viewBox="0 0 24 24"><circle cx="12" cy="12" r="12" fill="#fff"/><rect x="8.5" y="5" width="7" height="14" rx="1.3" fill="none" stroke="var(--brand-blue)" stroke-width="1.4"/><circle cx="12" cy="16.6" r="0.8" fill="var(--brand-blue)"/></svg>
        1-631-245-9073
      </li>
      <li class="contact-item">
        <svg class="contact-icon" viewBox="0 0 24 24"><circle cx="12" cy="12" r="12" fill="#fff"/><rect x="6" y="8" width="12" height="8.5" fill="var(--brand-blue)"/><path d="M6 8l6 5 6-5" fill="none" stroke="#fff" stroke-width="1.2"/></svg>
        marcus.pellow@corvanesupply.com
      </li>
      <li class="contact-item">
        <svg class="contact-icon" viewBox="0 0 24 24"><circle cx="12" cy="12" r="12" fill="#fff"/><g fill="none" stroke="var(--brand-blue)" stroke-width="1.1"><circle cx="12" cy="12" r="6.5"/><ellipse cx="12" cy="12" rx="2.8" ry="6.5"/><path d="M5.5 12h13M6.5 8.7h11M6.5 15.3h11"/></g></svg>
        www.corvanesupply.com
      </li>
    </ul>
  </section>

  <section class="card card-back">
    <div class="brand-mark">
      <div class="brand-dot"></div>
      <div class="brand-name">CORVANE SUPPLY</div>
    </div>
    <div class="divider"></div>
    <div class="back-url">
      <svg class="contact-icon" viewBox="0 0 24 24"><circle cx="12" cy="12" r="12" fill="var(--brand-blue)"/><g fill="none" stroke="#000" stroke-width="1.1"><circle cx="12" cy="12" r="6.5"/><ellipse cx="12" cy="12" rx="2.8" ry="6.5"/><path d="M5.5 12h13M6.5 8.7h11M6.5 15.3h11"/></g></svg>
      www.corvanesupply.com
    </div>
  </section>

</div>
</body>
</html>
```